Business card design for online Mandarin Learning School

We need a business card design for our online language learning school called "Maple Bridge Online for Mandarin Learning". Our existing website is https://www.maplebridgeonline.com
We have our logo already. We would like to see our business card design that can make our online teaching services to be innovative, young, energetic and fun to learn. Prefer to have a certain level of color matching with our website. Apart from "Maple Bridge Online", need to specifically state "for Mandarin Learning" as well on the business card.

```html
<!DOCTYPE html>
<html lang="en">
<head>
<meta charset="utf-8">
<title>Maple Bridge Online – Business Card</title>
<link href="https://fonts.googleapis.com/css2?family=Lato:wght@400;700&display=swap" rel="stylesheet">
<style>
  :root {
    --teal: #1a9ea6;
    --teal-deep: #0a8893;
    --teal-light: #52b5bb;
    --coral: #d9534f;
    --grey: #6f6f6f;
    --ink: #2b2b2b;
    --paper: #ffffff;
    --backdrop: #eeeeee;
  }
  * { margin: 0; padding: 0; box-sizing: border-box; }
  html, body { width: 1200px; height: 864px; overflow: hidden; }
  body {
    background: var(--backdrop);
    font-family: "Lato", sans-serif;
    position: relative;
  }
  .card {
    position: absolute;
    width: 530px;
    height: 303px;
    border-radius: 4px;
    box-shadow: 0 10px 28px rgba(0,0,0,0.12);
    overflow: hidden;
  }
  .card--front { left: 40px; top: 280px; background: var(--paper); }
  .card--back {
    left: 630px; top: 280px;
    background: linear-gradient(160deg, var(--teal-light) 0%, var(--teal) 55%, var(--teal-deep) 100%);
  }

  /* front */
  .brand {
    position: absolute;
    left: 28px; top: 116px;
    width: 180px;
    display: flex; align-items: center; gap: 9px;
  }
  .brand__dot {
    width: 12px; height: 12px; border-radius: 50%;
    background: var(--teal); flex: none;
  }
  .brand__name {
    color: var(--teal);
    font-size: 18px;
    font-weight: 400;
    letter-spacing: 1px;
    white-space: nowrap;
  }
  .divider {
    position: absolute;
    left: 222px; top: 34px;
    width: 1px; height: 190px;
    background: var(--grey);
  }
  .details { position: absolute; left: 244px; top: 30px; }
  .tagline { color: var(--teal); font-size: 17px; font-weight: 700; }
  .person { color: var(--coral); font-size: 21px; font-weight: 700; margin-top: 4px; }
  .role { color: var(--ink); font-size: 13px; margin-top: 1px; }
  .contacts { list-style: none; margin-top: 12px; }
  .contacts li {
    display: flex; align-items: center; gap: 8px;
    font-size: 12px; color: var(--ink);
    min-height: 22px;
    margin-bottom: 2px;
  }
  .contacts .org { line-height: 1.25; margin-bottom: 4px; }
  .org__name { color: var(--teal); display: block; }
  .org__type { color: var(--ink); display: block; }
  .icon {
    width: 18px; height: 18px; border-radius: 3px;
    background: var(--teal);
    display: flex; align-items: center; justify-content: center;
    flex: none;
  }
  .icon svg { width: 12px; height: 12px; }

  .bands { position: absolute; left: 0; bottom: 20px; width: 100%; height: 6px; display: flex; }
  .bands span:nth-child(1) { flex: 1; background: var(--grey); }
  .bands span:nth-child(2) { flex: 1.1; background: var(--coral); }
  .bands span:nth-child(3) { flex: 1; background: var(--teal); }
  .hairline { position: absolute; left: 0; bottom: 12px; width: 34%; height: 3px; background: var(--grey); }

  /* back */
  .back-mark {
    position: absolute; inset: 0;
    display: flex; align-items: center; justify-content: center; gap: 12px;
  }
  .back-mark__dot { width: 18px; height: 18px; border-radius: 50%; background: var(--paper); }
  .back-mark__name { color: var(--paper); font-size: 26px; font-weight: 400; letter-spacing: 2px; }
</style>
</head>
<body>

<section class="card card--front" aria-label="Business card front">
  <div class="brand">
    <span class="brand__dot"></span>
    <span class="brand__name">MAPLE BRIDGE</span>
  </div>
  <div class="divider"></div>
  <div class="details">
    <p class="tagline">For Mandarin Learning</p>
    <p class="person">Daniel Reed</p>
    <p class="role">Chief Executive</p>
    <ul class="contacts">
      <li class="org"><span class="icon"><svg viewBox="0 0 12 12"><path d="M6 1a3.5 3.5 0 0 0-3.5 3.5C2.5 7.5 6 11 6 11s3.5-3.5 3.5-6.5A3.5 3.5 0 0 0 6 1z" fill="none" stroke="#fff" stroke-width="1.2"/><circle cx="6" cy="4.5" r="1.2" fill="#fff"/></svg></span><span><span class="org__name">Maple Bridge Online</span><span class="org__type">Language School</span></span></li>
      <li><span class="icon"><svg viewBox="0 0 12 12"><path d="M3 1.5l1.8 2.2-1 1.1a6 6 0 0 0 3.4 3.4l1.1-1 2.2 1.8-1 1.5C5.5 10.5 1.5 6.5 1.5 2.5z" fill="#fff"/></svg></span>555-014-2297</li>
      <li><span class="icon"><svg viewBox="0 0 12 12"><rect x="1.5" y="3" width="9" height="6" fill="none" stroke="#fff" stroke-width="1.1"/><path d="M1.5 3L6 6.5 10.5 3" fill="none" stroke="#fff" stroke-width="1.1"/></svg></span>support@MapleBridgeOnline.com</li>
      <li><span class="icon"><svg viewBox="0 0 12 12"><circle cx="6" cy="6" r="4.5" fill="none" stroke="#fff" stroke-width="1"/><ellipse cx="6" cy="6" rx="2" ry="4.5" fill="none" stroke="#fff" stroke-width="1"/><path d="M1.5 6h9" stroke="#fff" stroke-width="1"/></svg></span>www.maplebridgeonline.com</li>
    </ul>
  </div>
  <div class="bands"><span></span><span></span><span></span></div>
  <div class="hairline"></div>
</section>

<section class="card card--back" aria-label="Business card back">
  <div class="back-mark">
    <span class="back-mark__dot"></span>
    <span class="back-mark__name">MAPLE BRIDGE</span>
  </div>
</section>

</body>
</html>
```